A design led business card for the construction industry

High-end business card to match logo. White logo on dark grey/off black to the front. Matching dark font on white to back, possibly with logo design again.

We offer construction and project management services to commercial and private clients in the UK. Projetcs range from newbuilds, conversion of listed buildings and refurbishments and extensions of existing homes. Our focus is on quality and attention to detail using the highest skills.

Contact Information for Business Card

Name; Dorian Hatch BSc
Position; Project Manager
Mobile; 07962 804 157
Tel; 01632 958412
email; dorian@framelark.co.uk
web; www.framelark.co.uk
Address; Ashcombe on Wey, KT4 7PZ

Colors

Designer to choose only greyscale colors for use in the design.

Requirements
Must have
• To include the below description of the business,

CONSTRUCTION - PROJECT MANAGEMENT
Nice to have
• The posibility of the top back of the card being used as a ruler. So will have a measurement to scale in mm or an architect scale of 1:50
Should not have
• Should not be portrait

```html
<!DOCTYPE html>
<html lang="en">
<head>
<meta charset="utf-8">
<title>Framelark business card</title>
<link href="https://fonts.googleapis.com/css2?family=Montserrat:wght@400;500&family=Roboto:wght@400;500&display=swap" rel="stylesheet">
<style>
  :root {
    --backdrop: #d3d8d8;
    --card: #151515;
    --ink: #dcdcdc;
    --ink-soft: #bdbdbd;
    --rule: #8a8a8a;
  }
  * { margin: 0; padding: 0; box-sizing: border-box; }
  html, body { width: 1200px; height: 1050px; overflow: hidden; }
  body {
    background: var(--backdrop);
    display: flex;
    flex-direction: column;
    align-items: center;
    justify-content: center;
    gap: 44px;
    font-family: "Roboto", Arial, sans-serif;
    color: var(--ink);
  }
  .card {
    width: 720px;
    height: 466px;
    background: var(--card);
    border-radius: 4px;
    position: relative;
  }

  /* Front */
  .card-front {
    display: flex;
    flex-direction: column;
    align-items: center;
    justify-content: center;
  }
  .brand {
    display: flex;
    align-items: center;
    gap: 22px;
  }
  .brand-mark {
    width: 30px;
    height: 30px;
    border: 2px solid var(--ink);
  }
  .brand-name {
    font-family: "Montserrat", Arial, sans-serif;
    font-weight: 400;
    font-size: 40px;
    letter-spacing: 14px;
    color: var(--ink);
  }
  .tagline {
    margin-top: 26px;
    font-family: "Montserrat", Arial, sans-serif;
    font-weight: 400;
    font-size: 14px;
    letter-spacing: 3px;
    color: var(--ink-soft);
  }

  /* Back */
  .card-back {
    display: flex;
    align-items: center;
    padding: 0 52px;
  }
  .back-brand {
    width: 290px;
    display: flex;
    flex-direction: column;
    align-items: center;
    gap: 18px;
  }
  .back-brand .brand-name { font-size: 28px; letter-spacing: 9px; }
  .back-brand .brand-mark { width: 26px; height: 26px; }
  .divider {
    width: 1.5px;
    height: 260px;
    background: var(--rule);
    margin: 0 36px 0 20px;
  }
  .contact { font-size: 19px; line-height: 1.3; }
  .contact-name { font-weight: 500; text-transform: uppercase; letter-spacing: 0.3px; }
  .contact-role { margin-bottom: 10px; }
  .contact-address { margin-bottom: 6px; }
  .contact-line { display: flex; align-items: center; gap: 10px; }
  .contact-line svg { width: 18px; height: 18px; flex: none; }
</style>
</head>
<body>

  <section class="card card-front">
    <div class="brand">
      <span class="brand-mark"></span>
      <span class="brand-name">FRAMELARK</span>
    </div>
    <p class="tagline">CONSTRUCTION - PROJECT MANAGEMENT</p>
  </section>

  <section class="card card-back">
    <div class="back-brand">
      <span class="brand-mark"></span>
      <span class="brand-name">FRAMELARK</span>
    </div>
    <div class="divider"></div>
    <div class="contact">
      <p class="contact-name">Dorian Hatch BSc</p>
      <p class="contact-role">Project Manager</p>
      <p class="contact-address">Ashcombe on Wey,<br>KT4 7PZ</p>
      <p class="contact-line">
        <svg viewBox="0 0 18 18" fill="none" stroke="currentColor" stroke-width="1.4"><rect x="5" y="1.5" width="8" height="15" rx="1.5"/><line x1="8" y1="14" x2="10" y2="14"/></svg>
        07962 804 157
      </p>
      <p class="contact-line">
        <svg viewBox="0 0 18 18" fill="currentColor"><path d="M2 6c0-2 3-3.5 7-3.5S16 4 16 6v1.5h-3.5V6h-7v1.5H2z"/><rect x="3.5" y="9" width="11" height="6.5" rx="1"/></svg>
        01632 958412
      </p>
      <p class="contact-line">
        <svg viewBox="0 0 18 18" fill="none" stroke="currentColor" stroke-width="1.4"><rect x="1.5" y="4" width="15" height="10" rx="1"/><polyline points="1.5,4 9,10 16.5,4"/></svg>
        dorian@framelark.co.uk
      </p>
      <p class="contact-line">
        <svg viewBox="0 0 18 18" fill="none" stroke="currentColor" stroke-width="1.3"><circle cx="9" cy="9" r="7.5"/><ellipse cx="9" cy="9" rx="3.2" ry="7.5"/><line x1="1.5" y1="9" x2="16.5" y2="9"/></svg>
        www.framelark.co.uk
      </p>
    </div>
  </section>

</body>
</html>
```